KDH Roofing Truck and Trailer Wrap

I need a graphic wrap on my Marvel Quarry pickup truck, and our 14' enclosed trailer

Target Market(s)

Home Owners

Industry/Entity Type

Roofing

Requirements
Must have
• RM Building Products and ZAV Logos
Nice to have
• Our services listed somewhere on the truck, maybe on the back tailgate and also on the sides at the very bottom of the doors: Roofing, Siding, Gutters, Painting

```html
<!DOCTYPE html>
<html lang="en">
<head>
<meta charset="UTF-8">
<title>Kendrick Home Services – Truck and Trailer Wrap</title>
<link rel="stylesheet" href="https://fonts.googleapis.com/css2?family=DM+Serif+Display&family=Poppins:wght@500;600;700&family=Oswald:wght@600&display=swap">
<style>
  :root {
    --ink: #111111;
    --paper: #ffffff;
    --canvas: #f4f4f4;
    --gold: #e0a21f;
    --gold-deep: #b8760f;
    --gold-light: #f6c85a;
    --gold-pale: #fbe3a6;
  }
  * { margin: 0; padding: 0; box-sizing: border-box; }
  html, body { width: 1200px; height: 1200px; overflow: hidden; background: var(--canvas); }
  .wrap-sheet { position: relative; width: 1200px; height: 1200px; }
  .wrap-panel {
    position: absolute; left: 50px; width: 1100px;
    background: var(--paper); overflow: hidden;
    box-shadow: 0 2px 10px rgba(0,0,0,0.12);
  }
  .wrap-panel--truck { top: 50px; height: 420px; }
  .wrap-panel--trailer { top: 520px; height: 600px; }
  .wrap-art { position: absolute; inset: 0; width: 100%; height: 100%; }

  .brand { position: absolute; display: flex; align-items: center; gap: 22px; }
  .brand-mark { background: var(--gold); flex: none; }
  .brand-name {
    font-family: "DM Serif Display", serif; color: var(--ink); line-height: 0.9;
  }
  .brand-tagline {
    font-family: "Poppins", sans-serif; font-weight: 600; color: var(--ink);
    letter-spacing: 0.22em; text-transform: uppercase; margin-top: 8px;
  }

  .service-list {
    position: absolute; display: flex; gap: 18px; list-style: none;
    font-family: "Poppins", sans-serif; font-weight: 700; color: var(--paper);
  }
  .service-list li { display: flex; align-items: center; gap: 7px; }
  .service-list li::before {
    content: ""; width: 9px; height: 9px; border-radius: 50%; background: var(--gold);
  }

  .contact { position: absolute; font-family: "Poppins", sans-serif; }
  .contact-web { font-weight: 600; }
  .contact-phone { font-family: "Oswald", sans-serif; font-weight: 600; letter-spacing: 0.06em; line-height: 1.1; }

  /* truck */
  .wrap-panel--truck .brand { left: 90px; top: 120px; }
  .wrap-panel--truck .brand-mark { width: 84px; height: 84px; }
  .wrap-panel--truck .brand-name { font-size: 92px; }
  .wrap-panel--truck .brand-tagline { font-size: 17px; }
  .wrap-panel--truck .service-list { left: 90px; top: 307px; font-size: 20px; }
  .wrap-panel--truck .contact { right: 40px; top: 46px; text-align: right; }
  .wrap-panel--truck .contact-web { color: var(--paper); font-size: 13px; }
  .wrap-panel--truck .contact-phone { color: var(--gold-light); font-size: 38px; }

  /* trailer */
  .wrap-panel--trailer .brand { left: 80px; top: 120px; }
  .wrap-panel--trailer .brand-mark { width: 110px; height: 110px; }
  .wrap-panel--trailer .brand-name { font-size: 122px; }
  .wrap-panel--trailer .brand-tagline { font-size: 22px; }
  .wrap-panel--trailer .service-list { left: 40px; top: 422px; font-size: 24px; }
  .wrap-panel--trailer .contact { left: 40px; top: 498px; }
  .wrap-panel--trailer .contact-web { color: var(--ink); font-size: 15px; }
  .wrap-panel--trailer .contact-phone { color: var(--ink); font-size: 46px; }
</style>
</head>
<body>
<main class="wrap-sheet">

  <section class="wrap-panel wrap-panel--truck" aria-label="Pickup truck side wrap">
    <svg class="wrap-art" viewBox="0 0 1100 420" aria-hidden="true">
      <defs>
        <linearGradient id="truckGold" x1="0" y1="0" x2="1" y2="1">
          <stop offset="0" stop-color="var(--gold-light)"/>
          <stop offset="0.55" stop-color="var(--gold)"/>
          <stop offset="1" stop-color="var(--gold-deep)"/>
        </linearGradient>
      </defs>
      <polygon points="640,420 700,365 955,128 1100,128 1100,420" fill="url(#truckGold)"/>
      <rect x="0" y="352" width="680" height="7" fill="var(--gold)"/>
      <polygon points="0,296 590,296 860,40 1100,40 1100,112 925,112 662,346 0,346" fill="var(--ink)"/>
      <polygon points="770,92 820,44 840,44 790,92" fill="var(--gold)"/>
    </svg>

    <div class="brand">
      <span class="brand-mark"></span>
      <div>
        <p class="brand-name">Kendrick</p>
        <p class="brand-tagline">Home Services</p>
      </div>
    </div>

    <ul class="service-list">
      <li>Roofing</li><li>Siding</li><li>Gutters</li><li>Painting</li>
    </ul>

    <div class="contact">
      <p class="contact-web">www.kendrickhomeservices.com</p>
      <p class="contact-phone">555-014-2287</p>
    </div>
  </section>

  <section class="wrap-panel wrap-panel--trailer" aria-label="Enclosed trailer side wrap">
    <svg class="wrap-art" viewBox="0 0 1100 600" aria-hidden="true">
      <defs>
        <linearGradient id="trailerGold" x1="0" y1="0" x2="1" y2="0.4">
          <stop offset="0" stop-color="var(--gold-pale)"/>
          <stop offset="0.45" stop-color="var(--gold-light)"/>
          <stop offset="0.8" stop-color="var(--gold)"/>
          <stop offset="1" stop-color="var(--gold-deep)"/>
        </linearGradient>
      </defs>
      <polygon points="0,486 712,486 1010,178 1100,178 1100,600 0,600" fill="url(#trailerGold)"/>
      <polygon points="0,408 630,408 960,30 1100,30 1100,158 995,158 712,470 0,470" fill="var(--ink)"/>
      <polygon points="830,120 905,38 935,38 860,120" fill="var(--gold)"/>
    </svg>

    <div class="brand">
      <span class="brand-mark"></span>
      <div>
        <p class="brand-name">Kendrick</p>
        <p class="brand-tagline">Home Services</p>
      </div>
    </div>

    <ul class="service-list">
      <li>Roofing</li><li>Siding</li><li>Gutters</li><li>Painting</li>
    </ul>

    <div class="contact">
      <p class="contact-web">www.kendrickhomeservices.com</p>
      <p class="contact-phone">555-014-2287</p>
    </div>
  </section>

</main>
</body>
</html>
```